Willow of Dawn Uniform Label Redesign

To refine our current product label designs into one, simple, modern, crisp, general look that can be adapted to all our all Natural Skin Care and Wellness products. I am inspired by the elegant versatility of products like Lumaveil Botanic Beauty or Fernly Beauty label schemes. We no longer want labels that indicate scent or ingredients. We have two primary colors that we want to maintain (#096CA3 and #DEE33F), and are willing to entertain subtle additions of others, other than black. Our labels will be printed on white or clear material. We use mainly Cosmo or Boston Round container shapes, plus flat top, smooth, round jars. Maybe a faded watermark highlight the "natural" or "beautiful" side of our products. we need to convey confidence, while remaining simple. We currently use the Advantage font. Maybe Century Gothic may work. Something similar that is easy on the eyes. Maybe vertical main text? We are willing to entertain a lot of ideas. These designs will offer ideas into our eventual Website (www.willowofdawnco.com) redesign.

Target Market(s)

Those who are familiar with the power of natural, plant based skin care and wellness products

Industry/Entity Type

Natural Skin Care and Wellness

Font styles to use
Sans Serif
Other font styles liked:
• Century Gothic, Advantage, or similar that is easy on the eyes

Colors
0054AA
0677BA
7BADD7
CADEEF
E8F1F8
59FF00
82FF00
B8FF75
E3FFCB
F4FFEA

Requirements
Must have
• "Clean Lines"; These colors: (#096CA3 and #DEE33F)
Nice to have
• MAYBE vertical main text or a watermark image

```html
<!DOCTYPE html>
<html lang="en">
<head>
<meta charset="utf-8">
<title>Willow of Dawn – Label System</title>
<link rel="stylesheet" href="https://fonts.googleapis.com/css2?family=Didact+Gothic&family=Fira+Sans+Condensed:wght@300;400&display=swap">
<style>
  :root {
    --brand-blue: #1f7bd6;
    --brand-lime: #c4ec2c;
    --ink: #2b2b2b;
    --ink-soft: #444;
    --paper: #ffffff;
    --board: #ffffff;
    --label-shadow: 4px 6px 10px rgba(0,0,0,0.18);
  }
  * { margin: 0; padding: 0; box-sizing: border-box; }
  html, body { width: 1200px; height: 848px; overflow: hidden; background: var(--board); }
  .board { position: relative; width: 1200px; height: 848px; }

  .label {
    position: absolute;
    background: var(--paper);
    box-shadow: var(--label-shadow);
    color: var(--ink);
  }
  .label > * { position: absolute; left: 0; right: 0; text-align: center; }

  .brand-mark { display: flex; flex-direction: column; align-items: center; }
  .brand-dot { border-radius: 50%; background: var(--brand-blue); }
  .brand-name {
    font-family: "Didact Gothic", sans-serif;
    color: var(--brand-blue);
    letter-spacing: 0.5px;
    white-space: nowrap;
  }
  .brand-descriptor {
    font-family: "Didact Gothic", sans-serif;
    color: var(--brand-lime);
    letter-spacing: 0.62em;
    padding-left: 0.62em;
  }
  .tagline {
    font-family: "Didact Gothic", sans-serif;
    color: var(--ink);
    letter-spacing: 1.6px;
  }
  .product-name {
    font-family: "Fira Sans Condensed", sans-serif;
    font-weight: 300;
    line-height: 1.3;
    color: var(--ink);
  }
  .rule {
    height: 3px;
    margin: 0 auto;
    background: linear-gradient(90deg, var(--brand-blue), var(--brand-lime));
  }
  .description-title {
    font-family: "Fira Sans Condensed", sans-serif;
    font-size: 10px;
    letter-spacing: 0.3px;
  }
  .description-copy {
    font-family: "Fira Sans Condensed", sans-serif;
    font-size: 9.4px;
    line-height: 13.2px;
    width: 182px;
    margin: 0 auto;
    text-align: justify;
    text-align-last: center;
    color: var(--ink-soft);
  }
  .volume {
    font-family: "Fira Sans Condensed", sans-serif;
    color: var(--ink);
  }
  .sparkle-accent {
    width: 56px; height: 56px;
    margin: 0 auto;
    border-radius: 50%;
    background: radial-gradient(circle, rgba(196,236,44,0.35), rgba(31,123,214,0.25) 60%, rgba(255,255,255,0) 72%);
  }

  /* Tall lotion label */
  .label--lotion { left: 230px; top: 64px; width: 312px; height: 722px; }
  .label--lotion .brand-mark { top: 104px; }
  .label--lotion .brand-dot { width: 30px; height: 30px; }
  .label--lotion .brand-name { top: 186px; font-size: 27px; }
  .label--lotion .brand-descriptor { top: 222px; font-size: 15px; }
  .label--lotion .tagline { top: 248px; font-size: 13px; }
  .label--lotion .rule--top { top: 293px; width: 123px; }
  .label--lotion .sparkle-accent { top: 321px; }
  .label--lotion .product-name { top: 393px; font-size: 23px; }
  .label--lotion .description-title { top: 489px; }
  .label--lotion .description-copy { top: 514px; }
  .label--lotion .rule--bottom { top: 621px; width: 123px; }
  .label--lotion .volume { top: 637px; font-size: 10px; }

  /* Square polish label */
  .size-note {
    position: absolute; left: 740px; top: 32px;
    font-family: "Didact Gothic", sans-serif; font-size: 12.5px; letter-spacing: 1px; color: var(--ink);
  }
  .label--polish { left: 738px; top: 66px; width: 374px; height: 381px; }
  .label--polish .brand-mark { top: 50px; }
  .label--polish .brand-dot { width: 26px; height: 26px; }
  .label--polish .brand-name { top: 103px; font-size: 30px; }
  .label--polish .brand-descriptor { top: 140px; font-size: 15px; }
  .label--polish .tagline { top: 169px; font-size: 12.5px; }
  .label--polish .product-name { top: 211px; font-size: 25px; }
  .label--polish .rule { top: 304px; width: 162px; }
  .label--polish .volume { top: 333px; font-size: 12.5px; }
</style>
</head>
<body>
<main class="board">

  <section class="label label--lotion" aria-label="Hydrating lotion label">
    <div class="brand-mark"><span class="brand-dot"></span></div>
    <h1 class="brand-name">WILLOW OF DAWN</h1>
    <p class="brand-descriptor">SKINCARE</p>
    <p class="tagline">Simple. Beautiful. Timeless.</p>
    <div class="rule rule--top"></div>
    <div class="sparkle-accent" role="img" aria-label="Small burst of blue and lime dots"></div>
    <h2 class="product-name">ALOE AND SHEA<br>HYDRATING LOTION</h2>
    <p class="description-title">DESCRIPTION</p>
    <p class="description-copy">Lorem ipsum dolor sit amet consectetuer odio non tellus natoque accumsan. Sed hac enim Lorem tempus tortor justo eget scelerisque sed morbi.</p>
    <div class="rule rule--bottom"></div>
    <p class="volume">8 fl. oz &nbsp;|&nbsp; 238ml &nbsp;&nbsp;℮</p>
  </section>

  <p class="size-note">4 x 4 inches</p>
  <section class="label label--polish" aria-label="Body polish label">
    <div class="brand-mark"><span class="brand-dot"></span></div>
    <h1 class="brand-name">WILLOW OF DAWN</h1>
    <p class="brand-descriptor">SKINCARE</p>
    <p class="tagline">Simple. Beautiful. Timeless.</p>
    <h2 class="product-name">SHEA AND SUGAR<br>BODY POLISH</h2>
    <div class="rule"></div>
    <p class="volume">4 fl. oz &nbsp;|&nbsp; 120ml &nbsp;&nbsp;℮</p>
  </section>

</main>
</body>
</html>
```